Brightwave Partners, Inc. Website redesign

Revamp the website, it is old and outdated. www.brightwavepartnersinc.example

Target Market(s)

Information Technology Consulting and Staffing

Coding

Coded - Design and coding required

Number of Pages Required

5+ page

Colors

Designer to choose colors to be used in the design.

Requirements
Must have
• Outlined text boxes just like from the Tolvane.us site. A clean look

```html
<!DOCTYPE html>
<html lang="en">
<head>
<meta charset="utf-8">
<title>Brightwave Partners, Inc.</title>
<link href="https://fonts.googleapis.com/css2?family=Audiowide&family=Lato:wght@400;700&display=swap" rel="stylesheet">
<style>
:root{
  --brand:#9b1230;
  --brand-dark:#7d0d25;
  --ink:#111111;
  --body:#555555;
  --band:#efefef;
  --line:#d7d7d7;
  --footer:#000000;
  --white:#ffffff;
}
*{box-sizing:border-box;margin:0;padding:0}
html,body{width:1200px;height:3574px;overflow:hidden}
body{position:relative;background:var(--white);font-family:'Lato',sans-serif;color:var(--body)}
.abs{position:absolute}
.display{font-family:'Audiowide',sans-serif}
.accent{color:var(--brand)}

/* hero */
.hero-bg{left:0;top:0;width:1200px;height:745px}
.logo{left:161px;top:24px;font-family:'Audiowide',sans-serif;font-size:34px;color:var(--white);line-height:40px;display:flex;align-items:center;gap:10px}
.logo .mark{width:26px;height:26px;background:var(--white)}
.nav{top:33px;left:0;width:1200px;font-family:'Audiowide',sans-serif;font-size:12.5px;color:var(--white)}
.nav span{position:absolute;white-space:nowrap}
.nav .active{border-bottom:1.5px solid var(--white);padding-bottom:3px}
.dot{width:14px;height:14px;border:1.5px solid var(--white);border-radius:50%;left:55px}
.dot.on::after{content:"";position:absolute;left:3px;top:3px;width:5px;height:5px;border-radius:50%;background:var(--white)}
.eyebrow{left:164px;top:172px;font-size:25px;color:var(--ink)}
.hero-title{left:164px;top:216px;font-size:47px;line-height:50px;color:var(--white)}
.hero-text{left:162px;top:338px;width:420px;font-size:13px;line-height:21px;color:var(--white)}
.btn-light{left:161px;top:458px;width:166px;height:52px;border:1.5px solid var(--white);color:var(--white);font-family:'Audiowide',sans-serif;font-size:18px;display:flex;align-items:center;justify-content:center}
.hero-photo{left:623px;top:115px;width:557px;height:443px;border-radius:8px;background:linear-gradient(160deg,#2c2c2c 0%,#5d6a78 35%,#b8b2ab 70%,#d9d9d9 100%)}

/* service circles */
.badge{width:76px;height:76px;border-radius:50%;background:var(--brand);border:3px solid var(--white);box-shadow:0 0 0 1.5px var(--brand);display:flex;align-items:center;justify-content:center}
.badge svg{width:42px;height:42px;fill:none;stroke:var(--white);stroke-width:2}
.badge-label{font-family:'Audiowide',sans-serif;font-size:12px;line-height:20px;color:var(--ink);text-align:center;width:160px}

/* sections */
.h2{font-family:'Audiowide',sans-serif;font-size:36px;color:var(--ink);line-height:44px}
.copy{font-size:12px;line-height:19.5px;color:var(--body)}
.btn{border:1.5px solid var(--brand);color:var(--brand);font-family:'Audiowide',sans-serif;font-size:13.5px;display:flex;align-items:center;justify-content:center;background:var(--white)}

.about-frame{left:814px;top:854px;width:225px;height:263px;background:var(--brand)}
.about-photo{left:652px;top:874px;width:368px;height:223px;background:linear-gradient(120deg,#3b3530 0%,#7b6a5c 40%,#c9c2bb 75%,#4a4f5c 100%)}

.band{left:0;top:1413px;width:1200px;height:300px}

.lead-frame{left:108px;top:1761px;width:226px;height:315px;background:var(--brand)}
.lead-photo{left:126px;top:1781px;width:339px;height:277px;background:linear-gradient(135deg,#0d2233 0%,#1f6f8f 45%,#0a1a28 100%)}
.lead-title{left:538px;top:1757px;font-size:34px;line-height:47px;color:var(--ink);width:560px}

.card{width:429px;height:350px;background:var(--white);box-shadow:0 0 8px rgba(0,0,0,.14)}
.card .img{position:absolute;left:0;top:0;width:429px;height:174px}
.card h3{position:absolute;left:12px;top:186px;font-family:'Audiowide',sans-serif;font-size:11px;color:var(--ink);width:410px}
.card .date{position:absolute;left:12px;top:203px;font-size:9.5px;color:var(--brand)}
.card p{position:absolute;left:12px;top:218px;width:405px;font-size:11.5px;line-height:19.5px;color:var(--body)}
.card .btn{position:absolute;left:11px;top:294px;width:105px;height:36px;font-size:12.5px}

.field{border:1.5px solid var(--line);font-size:11.5px;color:#777;padding:20px 16px 0}

/* contact band */
.contact-band{left:0;top:3122px;width:1200px;height:90px;background:var(--brand)}
.c-icon{top:3132px;width:66px;height:66px;background:var(--brand-dark);display:flex;align-items:center;justify-content:center}
.c-icon svg{width:34px;height:34px;fill:none;stroke:var(--white);stroke-width:2.4}
.c-small{font-size:11px;font-weight:700;color:#1b1b1b;white-space:nowrap}
.c-big{font-size:17px;font-weight:700;color:var(--white);white-space:nowrap}
.divider{top:3144px;width:1px;height:48px;background:rgba(255,255,255,.35)}

/* footer */
.footer{left:0;top:3212px;width:1200px;height:362px;background:var(--footer)}
.f-logo{left:0;width:1200px;top:3262px;display:flex;justify-content:center;align-items:center;gap:12px;font-family:'Audiowide',sans-serif;font-size:38px;color:var(--white)}
.f-logo .mark{width:30px;height:30px;background:var(--brand)}
.subscribe{left:0;width:1200px;top:3364px;text-align:center;font-family:'Audiowide',sans-serif;font-size:13px;color:var(--brand)}
.sub-input{left:442px;top:3397px;width:278px;height:36px;border:1px solid #cfcfcf;background:var(--footer);color:#ddd;font-size:11.5px;padding:11px 8px}
.sub-btn{left:720px;top:3397px;width:37px;height:36px;background:var(--white);display:flex;align-items:center;justify-content:center}
.f-nav span{position:absolute;top:3467px;font-size:12px;color:var(--white)}
.f-rule{left:161px;top:3519px;width:878px;height:1px;background:#444}
.copyright{left:161px;top:3538px;font-size:11.5px;color:var(--white)}
.social{top:3528px;width:34px;height:34px;border-radius:50%;border:1.5px solid var(--white)}
.social.filled{background:var(--brand);border-color:var(--brand)}
</style>
</head>
<body>

<!-- hero -->
<svg class="abs hero-bg" viewBox="0 0 1200 745" aria-hidden="true"><polygon points="0,0 1200,0 1200,583 0,745" fill="#9b1230"/></svg>
<div class="abs logo"><span>Brightwave</span><span class="mark"></span></div>
<nav class="abs nav">
  <span style="left:538px">Home</span>
  <span style="left:610px" class="active">About Us</span>
  <span style="left:700px">Services</span>
  <span style="left:791px">Strategy</span>
  <span style="left:879px">IT News</span>
  <span style="left:967px">Contact Us</span>
</nav>
<span class="abs dot" style="top:301px"></span>
<span class="abs dot on" style="top:347px"></span>
<span class="abs dot" style="top:391px"></span>
<span class="abs dot" style="top:429px"></span>
<div class="abs display eyebrow">BRIGHTWAVE PARTNERS</div>
<h1 class="abs display hero-title">Mission Integrity<br>Results</h1>
<p class="abs hero-text">Brightwave Partners, Inc. is an 8(a) full-service IT consulting company based in the Washington, DC Metro area. We offer specialized, highly customized technology solutions for our customers located throughout the United States.</p>
<div class="abs btn-light">Let’s Started</div>
<div class="abs hero-photo" role="img" aria-label="Desktop monitor showing colleagues working together at computers"></div>

<!-- services -->
<div class="abs badge" style="left:171px;top:674px"><svg viewBox="0 0 42 42"><rect x="6" y="9" width="24" height="17" rx="1"/><rect x="24" y="15" width="12" height="19" rx="1"/><path d="M13 32h10M18 26v6"/></svg></div>
<div class="abs badge-label" style="left:130px;top:752px">Hardware /<br>Software Sales</div>
<div class="abs badge" style="left:381px;top:658px"><svg viewBox="0 0 42 42"><circle cx="21" cy="21" r="7"/><circle cx="21" cy="21" r="13" stroke-dasharray="5 3"/></svg></div>
<div class="abs badge-label" style="left:340px;top:737px">Professional<br>Services</div>
<div class="abs badge" style="left:592px;top:621px"><svg viewBox="0 0 42 42"><circle cx="21" cy="22" r="6"/><circle cx="9" cy="31" r="3"/><circle cx="33" cy="31" r="3"/><circle cx="21" cy="8" r="3"/><path d="M21 11v5M12 29l5-3M30 29l-5-3"/></svg></div>
<div class="abs badge-label" style="left:550px;top:699px">Technology<br>Assessment</div>
<div class="abs badge" style="left:801px;top:590px"><svg viewBox="0 0 42 42"><rect x="18" y="6" width="18" height="13"/><path d="M22 16v-4M26 16v-6M30 16v-3"/><circle cx="11" cy="22" r="3"/><circle cx="21" cy="26" r="3"/><path d="M5 34c0-4 3-7 6-7s6 3 6 7M15 36c0-4 3-6 6-6s6 2 6 6"/></svg></div>
<div class="abs badge-label" style="left:760px;top:668px">Technology<br>Consulting</div>

<!-- about -->
<h2 class="abs h2" style="left:164px;top:853px">About <span class="accent">Us</span></h2>
<p class="abs copy" style="left:162px;top:915px;width:410px">Brightwave Partners, Inc. is an 8(a) innovative and rapidly growing full-service IT consulting firm. We provide our clients with cutting-edge technologies and the know-how to apply them to their individual business models.</p>
<p class="abs copy" style="left:162px;top:993px;width:410px">For over 20 + years, we have been providing reliable IT solutions to businesses in the Washington, DC Metro area and beyond. Our comprehensive services provide clients with unique technology solutions that are customized to meet the specific demands of their business.</p>
<div class="abs btn" style="left:161px;top:1105px;width:113px;height:38px">Know More</div>
<div class="abs about-frame"></div>
<div class="abs about-photo" role="img" aria-label="Team of colleagues reviewing work on a laptop"></div>

<!-- strategy -->
<h2 class="abs h2" style="left:0;width:1200px;text-align:center;top:1211px">Our <span class="accent">Strategy</span></h2>
<p class="abs copy" style="left:284px;top:1283px;width:614px;text-align:center">Civilian and Federal agencies are facing increased demands driven by the changing economic environment and shifts in the way products and services are sold and delivered. These factors have created an imperative to leverage new and innovative technology solution architectures like cloud computing to help reduce cost and deliver profit-driving IT capabilities faster than ever before. Savvy businesses understand that technology investments cannot be made solely to enable internal and external operations; technology is now, more than ever, a critical component to retaining and winning customers as well as staying ahead of the competition.</p>

<svg class="abs band" viewBox="0 0 1200 300" aria-hidden="true"><polygon points="0,74 1200,0 1200,224 0,300" fill="#efefef"/></svg>
<div class="abs badge" style="left:171px;top:1554px"><svg viewBox="0 0 42 42"><path d="M12 36v-8c-4-3-5-8-3-13 3-6 11-8 17-5 5 3 7 9 4 14l3 5h-4v4h-6v3"/><circle cx="21" cy="18" r="4"/></svg></div>
<div class="abs badge-label" style="left:130px;top:1634px">Assess</div>
<div class="abs badge" style="left:367px;top:1532px"><svg viewBox="0 0 42 42"><rect x="10" y="6" width="22" height="30" rx="1"/><path d="M15 13h12M15 19h12M15 25h6"/><circle cx="26" cy="28" r="4"/></svg></div>
<div class="abs badge-label" style="left:325px;top:1610px">Recommend</div>
<div class="abs badge" style="left:561px;top:1509px"><svg viewBox="0 0 42 42"><rect x="7" y="8" width="28" height="26" rx="1"/><path d="M12 28v-6M17 28v-10M22 28v-8M27 28v-13"/></svg></div>
<div class="abs badge-label" style="left:519px;top:1588px">Implement</div>
<div class="abs badge" style="left:757px;top:1486px"><svg viewBox="0 0 42 42"><rect x="6" y="8" width="30" height="20" rx="1"/><path d="M16 34h10M21 28v6M11 22l6-6 5 4 8-8"/></svg></div>
<div class="abs badge-label" style="left:715px;top:1566px">Monitor</div>
<div class="abs badge" style="left:951px;top:1464px"><svg viewBox="0 0 42 42"><circle cx="24" cy="18" r="9"/><circle cx="24" cy="18" r="4"/><path d="M17 25 7 35"/></svg></div>
<div class="abs badge-label" style="left:909px;top:1543px">Manage</div>

<!-- thought leadership -->
<div class="abs lead-frame"></div>
<div class="abs lead-photo" role="img" aria-label="Rows of network servers with blue status lights"></div>
<h2 class="abs display lead-title">Bringing Thought Leadership<br>and Quality to <span class="accent">Every Project</span></h2>
<p class="abs copy" style="left:538px;top:1856px;width:470px">Brightwave Partners, Inc. is an 8(a) full-service IT consulting company based in the Washington, DC Metro area. We offer specialized, highly customized technology solutions for our customers located throughout the United State.</p>
<p class="abs copy" style="left:538px;top:1934px;width:470px">No two businesses are the same. We believe the technology supporting your business operations should align with your company. Every project begins with a thorough analysis of your current technology environment.</p>
<div class="abs btn" style="left:535px;top:2040px;width:114px;height:37px">Read More</div>

<!-- news -->
<h2 class="abs h2" style="left:0;width:1200px;text-align:center;top:2156px">Our <span class="accent">News</span></h2>
<article class="abs card" style="left:161px;top:2248px">
  <div class="img" role="img" aria-label="Network cables plugged into a server rack" style="background:linear-gradient(135deg,#1c2024 0%,#3d464e 50%,#7e8990 100%)"></div>
  <h3>Lorem Ipsum is simply dummy text of the printing and typesetting</h3>
  <div class="date">4 September 2019</div>
  <p>Lorem Ipsum is simply dummy text of the printing and typesetting industry. Lorem Ipsum has been the industry's standard dummy text ever since the 1500s</p>
  <div class="btn">Read More</div>
</article>
<article class="abs card" style="left:610px;top:2248px">
  <div class="img" role="img" aria-label="Developer working at a desktop computer" style="background:linear-gradient(120deg,#2a3442 0%,#8aa0b5 45%,#e6e1da 100%)"></div>
  <h3>Lorem Ipsum is simply dummy text of the printing and typesetting</h3>
  <div class="date">4 September 2019</div>
  <p>Lorem Ipsum is simply dummy text of the printing and typesetting industry. Lorem Ipsum has been the industry's standard dummy text ever since the 1500s</p>
  <div class="btn">Read More</div>
</article>

<!-- contact -->
<h2 class="abs h2" style="left:0;width:1200px;text-align:center;top:2673px">Contact <span class="accent">Us</span></h2>
<div class="abs field" style="left:304px;top:2756px;width:285px;height:44px;padding-top:14px">Name:</div>
<div class="abs field" style="left:610px;top:2756px;width:285px;height:44px;padding-top:14px">Email:</div>
<div class="abs field" style="left:304px;top:2816px;width:285px;height:44px;padding-top:14px">Phone:</div>
<div class="abs field" style="left:610px;top:2816px;width:285px;height:44px;padding-top:14px">Subject:</div>
<div class="abs field" style="left:304px;top:2875px;width:591px;height:90px;padding-top:12px">Message:</div>
<div class="abs btn" style="left:535px;top:3021px;width:130px;height:38px">Drop Message</div>

<div class="abs contact-band"></div>
<div class="abs c-icon" style="left:172px"><svg viewBox="0 0 34 34"><path d="M8 5l5 1 2 6-3 2c2 4 4 6 8 8l2-3 6 2 1 5c-1 2-3 3-5 3C14 28 6 20 5 10c0-2 1-4 3-5z"/></svg></div>
<div class="abs c-small" style="left:248px;top:3142px">Call Us On:</div>
<div class="abs c-big" style="left:248px;top:3163px">555-014-2290</div>
<div class="abs divider" style="left:451px"></div>
<div class="abs c-icon" style="left:473px"><svg viewBox="0 0 34 34"><rect x="4" y="8" width="26" height="18"/><path d="M4 8l13 11 13-11M4 26l10-9M30 26l-10-9"/></svg></div>
<div class="abs c-small" style="left:548px;top:3142px">Mail Us:</div>
<div class="abs c-big" style="left:548px;top:3163px">info@bwpartners.example</div>
<div class="abs divider" style="left:750px"></div>
<div class="abs c-icon" style="left:773px"><svg viewBox="0 0 34 34"><path d="M17 31s-9-10-9-17a9 9 0 0 1 18 0c0 7-9 17-9 17z"/><circle cx="17" cy="14" r="3"/></svg></div>
<div class="abs c-big" style="left:849px;top:3141px;line-height:24px">220 Harborview Ln<br>Calder, MD 20999</div>

<!-- footer -->
<div class="abs footer"></div>
<div class="abs f-logo"><span>Brightwave</span><span class="mark"></span></div>
<div class="abs subscribe">Subscribe To Our Newsletter</div>
<div class="abs sub-input">Enter Email:</div>
<div class="abs sub-btn"><svg width="20" height="20" viewBox="0 0 20 20"><path d="M2 10 18 3l-4 15-4-5-5 3 2-5z" fill="#9b1230"/></svg></div>
<nav class="f-nav">
  <span style="left:391px">Home</span>
  <span style="left:453px">About Us</span>
  <span style="left:530px">Services</span>
  <span style="left:605px">Strategy</span>
  <span style="left:676px">IT News</span>
  <span style="left:750px">Contact Us</span>
</nav>
<div class="abs f-rule"></div>
<div class="abs copyright">© 2019 Brightwave Partners, All Rights Reserved. Terms &amp; Conditions | Privacy Policy.</div>
<span class="abs social" style="left:869px"></span>
<span class="abs social filled" style="left:915px"></span>
<span class="abs social" style="left:961px"></span>
<span class="abs social" style="left:1005px"></span>

</body>
</html>
```